Landingpage design for Carvelotrader website

We need a design for a responsive 1 page landing page.
Good example: https://www.frelvana.com/
On the homepage we will like to have a explanation video
attached you can find the logo's

About the website Carvelo.hub:
Carvelo.hub is a “Broker” we bring buyers and sellers together and facilitate transactions

Simple
quickly
Actuel
Compare (who is the best provider, at what price)
great offer
independent
1 invoice

Target Market(s)

BtoB

Number of Pages Required

1 page

Requirements
Must have
• On the homepage we will like to have a explanation video
Nice to have
• something between shipper and carrier and bring them togheter
• We will focus us first on fish transport... maybe you can add something
• Map from europe that shows our workarea

```html
<!DOCTYPE html>
<html lang="en">
<head>
<meta charset="utf-8">
<title>Carvelo Hub – Landing Page</title>
<link rel="stylesheet" href="https://fonts.googleapis.com/css2?family=Montserrat:wght@400;600;700&family=Open+Sans:wght@400;600;700&display=swap">
<style>
:root{
  --blue:#2fa6d8;
  --blue-dark:#1f8fc2;
  --ink:#1d1d1d;
  --text:#2b2b2b;
  --muted:#f5f5f5;
  --white:#ffffff;
  --footer-dark:#2a2a2a;
  --green:#6dbb2f;
  --pill:#3a3a3a;
}
*{box-sizing:border-box;margin:0;padding:0}
html,body{width:1200px;height:3719px;overflow:hidden;background:var(--white)}
body{position:relative;font-family:"Open Sans",sans-serif;color:var(--text)}
.abs{position:absolute}
h2,h3,.nav,.stat-num,.stat-label,.btn{font-family:"Montserrat",sans-serif}

/* header */
.site-header{position:absolute;left:0;top:0;width:1200px;height:124px;background:var(--white)}
.brand{position:absolute;left:0;top:0;width:372px;height:124px;background:var(--blue);display:flex;align-items:center;padding-left:52px;gap:18px}
.brand-mark{width:44px;height:44px;border-radius:50%;border:4px solid var(--white)}
.brand-name{color:var(--white);font-family:"Montserrat",sans-serif;font-weight:600;font-size:28px;line-height:30px;text-transform:uppercase}
.account{position:absolute;top:0;height:32px;font-size:17px;color:var(--white);display:flex;align-items:center;justify-content:center;font-family:"Montserrat",sans-serif}
.account.login{left:843px;width:144px;background:var(--blue)}
.account.register{left:1001px;width:147px;background:var(--ink)}
.nav{position:absolute;top:52px;left:490px;font-size:15px;color:var(--blue);letter-spacing:.5px}
.nav a{position:absolute;white-space:nowrap;text-decoration:none;color:var(--blue)}
.nav a.active{color:var(--ink)}
.nav a.active::after{content:"";position:absolute;left:0;right:0;bottom:-10px;height:4px;background:var(--ink)}

/* hero */
.hero{position:absolute;left:0;top:124px;width:1200px;height:546px;background:var(--muted)}
.check-pill{position:absolute;left:64px;height:54px;display:flex;align-items:center}
.check-pill .tick{width:54px;height:54px;border-radius:50%;background:var(--green);border:4px solid #dcdcdc;position:relative;z-index:2}
.check-pill .label{margin-left:-14px;background:var(--pill);color:var(--white);height:36px;border-radius:0 18px 18px 0;padding:0 40px 0 30px;display:flex;align-items:center;font-size:14px;font-weight:600;width:390px}
.hero-copy{position:absolute;left:77px;top:216px;width:400px;font-size:21px;line-height:26px;color:var(--ink)}
.hero-copy p+p{margin-top:20px}
.btn{position:absolute;height:40px;background:var(--blue);color:var(--white);font-size:14px;font-weight:700;font-style:italic;display:flex;align-items:center;padding-left:22px;border-radius:3px}
.btn svg{position:absolute;right:12px;top:10px}
.video{position:absolute;left:565px;top:74px;width:565px;height:392px;background:#fff;box-shadow:0 6px 14px rgba(0,0,0,.25)}
.video-frame{position:absolute;left:12px;top:12px;width:541px;height:340px;background:linear-gradient(180deg,#56657a 0%,#8d99a6 45%,#3d4650 100%)}
.video-controls{position:absolute;left:12px;top:352px;width:541px;height:28px;background:linear-gradient(#e8e8e8,#bdbdbd)}
.dots{position:absolute;left:578px;top:515px;display:flex;gap:14px}
.dots span{width:13px;height:13px;border-radius:50%;background:var(--blue)}

/* stats */
.stats{position:absolute;left:0;top:674px;width:1200px;height:243px;background:linear-gradient(180deg,#6fc6e6,#4fb3dc)}
.stat{position:absolute;width:300px;text-align:center}
.stat-ring{width:128px;height:128px;border-radius:50%;border:4px solid var(--white);margin:0 auto;display:flex;align-items:center;justify-content:center}
.stat-num{color:var(--white);font-size:34px;font-weight:600}
.stat-label{color:var(--white);font-size:16px;font-weight:700;margin-top:20px;letter-spacing:.5px}

/* feature rows */
.feature{position:absolute;left:0;width:1200px}
.feature.grey{background:var(--muted)}
.feature h2{position:absolute;font-size:22px;font-weight:700;color:var(--ink);white-space:nowrap}
.feature h2::after{content:"";position:absolute;left:0;top:42px;width:120px;height:3px;background:var(--blue)}
.feature .copy{position:absolute;width:430px;font-size:16px;line-height:23px;color:var(--text)}
.feature .copy p+p{margin-top:23px}
.media{position:absolute;overflow:hidden}
.media.right-round{border-radius:0 215px 215px 0}
.media.left-round{border-radius:215px 0 0 215px}
.media .ring{position:absolute;border:4px solid rgba(255,255,255,.9);border-radius:50%}

/* contact */
.contact-map{position:absolute;left:99px;top:2955px;width:484px;height:263px;background:linear-gradient(135deg,#e9e4d4,#d6dfc3 60%,#c9d8e6);border:1px solid #ccc}
.contact h2{position:absolute;left:640px;top:2960px;font-size:22px;font-weight:700;color:var(--ink)}
.contact h2::after{content:"";position:absolute;left:0;top:40px;width:120px;height:3px;background:var(--blue)}
.contact .intro{position:absolute;left:640px;top:3013px;width:440px;font-size:16px;line-height:23px}
.contact dl{position:absolute;left:640px;top:3083px;font-size:14px;line-height:19px;display:grid;grid-template-columns:76px 16px auto}

/* footer */
.site-footer{position:absolute;left:0;top:3267px;width:1200px;height:382px;background:var(--blue)}
.footer-brand{position:absolute;left:62px;top:55px;display:flex;align-items:center;gap:14px}
.footer-brand .brand-mark{width:34px;height:34px;border-width:3px}
.footer-brand span{color:var(--white);font-family:"Montserrat",sans-serif;font-weight:600;font-size:21px;line-height:22px;text-transform:uppercase}
.f-icon{position:absolute;width:70px;height:70px;border-radius:50%;background:var(--white);display:flex;align-items:center;justify-content:center}
.f-col{position:absolute;width:230px;color:var(--white)}
.f-col h3{font-size:17px;font-weight:600;margin-bottom:6px;display:flex;align-items:center;gap:8px}
.f-col h3 i{width:20px;height:20px;border-radius:50%;border:2px solid var(--white);display:inline-block}
.f-col p{font-size:13px;line-height:21px;font-weight:700}
.bottom-bar{position:absolute;left:0;top:3649px;width:1200px;height:70px;background:var(--footer-dark);color:var(--white);font-size:14px}
.bottom-bar p{position:absolute;left:99px;top:25px}
.social{position:absolute;left:852px;top:20px;display:flex;gap:10px}
.social span{width:30px;height:30px;border-radius:50%;background:var(--white)}
</style>
</head>
<body>

<header class="site-header">
  <div class="brand"><span class="brand-mark"></span><span class="brand-name">Carvelo<br>Hub</span></div>
  <a class="account login">Login</a>
  <a class="account register">Register</a>
  <nav class="nav">
    <a class="active" style="left:0">HOME</a>
    <a style="left:88px">ABOUT US</a>
    <a style="left:228px">PRICING</a>
    <a style="left:360px">FAQ</a>
    <a style="left:442px">CONTACT</a>
    <a style="left:566px"><svg width="22" height="22" viewBox="0 0 22 22"><circle cx="9" cy="9" r="6.5" fill="none" stroke="#2fa6d8" stroke-width="2.5"/><line x1="14" y1="14" x2="20" y2="20" stroke="#2fa6d8" stroke-width="3"/></svg></a>
    <a style="left:640px"><svg width="24" height="20" viewBox="0 0 24 20"><rect y="3" width="24" height="2.5" fill="#2fa6d8"/><rect y="9" width="24" height="2.5" fill="#2fa6d8"/><rect y="15" width="24" height="2.5" fill="#2fa6d8"/></svg></a>
  </nav>
</header>

<section class="hero">
  <div class="check-pill" style="top:74px"><span class="tick"><svg width="46" height="46" viewBox="0 0 46 46"><path d="M12 24 l8 8 l15-18" fill="none" stroke="#fff" stroke-width="5" stroke-linecap="round"/></svg></span><span class="label">Looking For a Tranport Company ?</span></div>
  <div class="check-pill" style="top:149px"><span class="tick"><svg width="46" height="46" viewBox="0 0 46 46"><path d="M12 24 l8 8 l15-18" fill="none" stroke="#fff" stroke-width="5" stroke-linecap="round"/></svg></span><span class="label">Looking For a Loading ?</span></div>
  <div class="hero-copy">
    <p>We Bring you together and find the bestand most efficient way for your shipment.</p>
    <p>You are a view steps away from the easiest way to organize your transports</p>
  </div>
  <a class="btn" style="left:77px;top:424px;width:216px">Get a Free Estimate<svg width="26" height="20" viewBox="0 0 26 20"><path d="M2 10h20M14 2l8 8-8 8" fill="none" stroke="#fff" stroke-width="3"/></svg></a>
  <a class="btn" style="left:310px;top:424px;width:213px">Become a Carrier<svg width="26" height="20" viewBox="0 0 26 20"><path d="M2 10h20M14 2l8 8-8 8" fill="none" stroke="#fff" stroke-width="3"/></svg></a>
  <div class="video">
    <div class="video-frame" role="img" aria-label="Explanation video still: a truck on a coastal road">
      <svg class="abs" style="left:245px;top:145px" width="52" height="56" viewBox="0 0 52 56"><path d="M4 2 L50 28 L4 54 Z" fill="#fff" opacity=".9"/></svg>
    </div>
    <div class="video-controls"><svg width="541" height="28"><rect x="12" y="8" width="12" height="12" fill="#555"/><rect x="120" y="12" width="300" height="4" fill="#888"/><rect x="500" y="8" width="24" height="12" fill="#555"/></svg></div>
  </div>
  <div class="dots"><span></span><span></span><span></span><span></span></div>
</section>

<section class="stats" role="img" aria-label="Blue-tinted band with trucks in the background">
  <div class="stat" style="left:98px;top:45px"><div class="stat-ring"><span class="stat-num">3.5M</span></div><div class="stat-label">SHIPPING CUSTOMERS</div></div>
  <div class="stat" style="left:445px;top:45px"><div class="stat-ring"><span class="stat-num">9.5M</span></div><div class="stat-label">SERVICE PROVIDERS</div></div>
  <div class="stat" style="left:787px;top:45px"><div class="stat-ring"><span class="stat-num">8.5M</span></div><div class="stat-label">SHIPMENT LISTINGS</div></div>
</section>

<section class="feature" style="top:967px;height:433px">
  <div class="media right-round" style="left:0;top:0;width:615px;height:433px;background:linear-gradient(135deg,#c9d6e2,#7b8794 50%,#3b4148)" role="img" aria-label="Photo of a truck driving past snowy mountains">
    <span class="ring" style="left:150px;top:50px;width:440px;height:330px"></span>
  </div>
  <h2 style="left:679px;top:36px">Why should i use carvelo hub?</h2>
  <div class="copy" style="left:679px;top:86px">
    <p>Lorem Ipsum is simply dummy text of the printing and typesetting industry. Lorem Ipsum has been the industry's standard dummy text ever since the 1500s, when an unknown printer took a galley of type and a type specimen book.</p>
    <p>It has survived not only five centuries, but also the leap into electronic typesetting, remaining essentially unchanged. It was popularised in the 1960s with the like Aldus PageMaker including versions of Lorem Ipsum.</p>
  </div>
  <a class="btn" style="left:681px;top:368px;width:156px">Read more<svg width="26" height="20" viewBox="0 0 26 20"><path d="M2 10h20M14 2l8 8-8 8" fill="none" stroke="#fff" stroke-width="3"/></svg></a>
</section>

<section class="feature grey" style="top:1463px;height:465px">
  <h2 style="left:104px;top:42px">Transport Solutions</h2>
  <div class="copy" style="left:104px;top:92px">
    <p>Lorem Ipsum is simply dummy text of the printing and typesetting industry. Lorem Ipsum has been the industry's standard dummy text ever since the 1500s, when an unknown printer took a galley of type and a type specimen book.</p>
    <p>It has survived not only five centuries, but also the leap into electronic typesetting, remaining essentially unchanged. It was popularised in the 1960s with the like Aldus PageMaker including versions of Lorem Ipsum.</p>
  </div>
  <a class="btn" style="left:104px;top:374px;width:156px">Read more<svg width="26" height="20" viewBox="0 0 26 20"><path d="M2 10h20M14 2l8 8-8 8" fill="none" stroke="#fff" stroke-width="3"/></svg></a>
  <div class="media left-round" style="left:669px;top:19px;width:531px;height:427px;background:linear-gradient(135deg,#e9b36a,#c98a3f 55%,#8a5a26)" role="img" aria-label="Photo of stacked cardboard boxes on a pallet">
    <span class="ring" style="left:40px;top:40px;width:420px;height:350px"></span>
  </div>
</section>

<section class="feature" style="top:1966px;height:426px">
  <div class="media right-round" style="left:0;top:0;width:615px;height:426px;background:linear-gradient(135deg,#dfe7c9,#e9e2cf 50%,#c7dbe9)" role="img" aria-label="Map of Europe showing the work area">
    <span class="ring" style="left:150px;top:40px;width:440px;height:340px;border-color:rgba(255,255,255,.8)"></span>
  </div>
  <h2 style="left:679px;top:30px">Destanition Europe</h2>
  <div class="copy" style="left:679px;top:80px">
    <p>Lorem Ipsum is simply dummy text of the printing and typesetting industry. Lorem Ipsum has been the industry's standard dummy text ever since the 1500s, when an unknown printer took a galley of type and a type specimen book.</p>
    <p>It has survived not only five centuries, but also the leap into electronic typesetting, remaining essentially unchanged. It was popularised in the 1960s with the like Aldus PageMaker including versions of Lorem Ipsum.</p>
  </div>
  <a class="btn" style="left:681px;top:362px;width:156px">Read more<svg width="26" height="20" viewBox="0 0 26 20"><path d="M2 10h20M14 2l8 8-8 8" fill="none" stroke="#fff" stroke-width="3"/></svg></a>
</section>

<section class="feature grey" style="top:2429px;height:467px">
  <h2 style="left:104px;top:42px">Free ?</h2>
  <div class="copy" style="left:104px;top:92px">
    <p>Lorem Ipsum is simply dummy text of the printing and typesetting industry. Lorem Ipsum has been the industry's standard dummy text ever since the 1500s, when an unknown printer took a galley of type and a type specimen book.</p>
    <p>It has survived not only five centuries, but also the leap into electronic typesetting, remaining essentially unchanged. It was popularised in the 1960s with the like Aldus PageMaker including versions of Lorem Ipsum.</p>
  </div>
  <a class="btn" style="left:104px;top:376px;width:156px">Read more<svg width="26" height="20" viewBox="0 0 26 20"><path d="M2 10h20M14 2l8 8-8 8" fill="none" stroke="#fff" stroke-width="3"/></svg></a>
  <div class="abs" style="left:719px;top:87px;width:347px;height:273px;background:linear-gradient(160deg,#444,#2a2a2a 70%,#f5f5f5 100%);border-radius:20px;transform:rotate(-18deg)" role="img" aria-label="Illustration of a dark price tag reading free with an orange string"></div>
</section>

<section class="contact">
  <div class="contact-map" role="img" aria-label="Street map with a location pin for the office"></div>
  <h2>Contact us</h2>
  <p class="intro">Lorem Ipsum is simply dummy text of the printing and typesetting industry.</p>
  <dl>
    <dt>Address</dt><dd>:</dd><dd>123 Street, City Name, DC 12345</dd>
    <dt>Phone</dt><dd>:</dd><dd>+ 123 456 7890</dd>
    <dt>Fax</dt><dd>:</dd><dd>+ 123 456 7890</dd>
    <dt>Email</dt><dd>:</dd><dd>info@carvelohub.com</dd>
    <dt>Skype</dt><dd>:</dd><dd>Carvelo Hub</dd>
  </dl>
</section>

<footer class="site-footer">
  <div class="footer-brand"><span class="brand-mark"></span><span>Carvelo<br>Hub</span></div>
  <span class="f-icon" style="left:416px;top:54px"><svg width="34" height="34" viewBox="0 0 34 34"><path d="M8 20a10 10 0 1 0 3-11" fill="none" stroke="#2fa6d8" stroke-width="4"/><path d="M6 4v9h9" fill="none" stroke="#2fa6d8" stroke-width="4"/></svg></span>
  <span class="f-icon" style="left:669px;top:54px"><svg width="34" height="30" viewBox="0 0 34 30"><rect x="2" y="3" width="30" height="24" rx="2" fill="none" stroke="#2fa6d8" stroke-width="3"/><rect x="7" y="8" width="9" height="8" fill="#2fa6d8"/><line x1="19" y1="10" x2="28" y2="10" stroke="#2fa6d8" stroke-width="2.5"/><line x1="7" y1="21" x2="28" y2="21" stroke="#2fa6d8" stroke-width="2.5"/></svg></span>
  <span class="f-icon" style="left:927px;top:54px"><svg width="28" height="30" viewBox="0 0 28 30"><rect x="2" y="2" width="24" height="26" rx="2" fill="#2fa6d8"/><line x1="7" y1="10" x2="21" y2="10" stroke="#fff" stroke-width="2.5"/><line x1="7" y1="15" x2="21" y2="15" stroke="#fff" stroke-width="2.5"/><line x1="7" y1="20" x2="21" y2="20" stroke="#fff" stroke-width="2.5"/></svg></span>

  <div class="f-col" style="left:99px;top:136px"><h3>Contact us</h3><p>Lorem Ipsum is simply dummy text of the printing and typesetting industry.</p></div>
  <div class="f-col" style="left:421px;top:136px"><h3>Want more ?</h3><p>Lorem Ipsum is simply dummy text of the printing and typesetting industry.</p></div>
  <div class="f-col" style="left:674px;top:136px"><h3>Press</h3><p>Lorem Ipsum is simply dummy text of the printing and typesetting industry.</p></div>
  <div class="f-col" style="left:937px;top:136px"><h3>Blog</h3><p>Lorem Ipsum is simply dummy text of the printing and typesetting industry.</p></div>

  <div class="f-col" style="left:99px;top:255px"><h3><i></i>Services</h3><p>Lorem Ipsum is simply dummy text of the printing</p></div>
  <div class="f-col" style="left:421px;top:255px"><h3><i></i>Foundation</h3><p>Lorem Ipsum is simply dummy text of the printing</p></div>
  <div class="f-col" style="left:674px;top:255px"><h3><i></i>Carvelo Hub Apps</h3><p>Lorem Ipsum is simply dummy text of the printing</p></div>
  <div class="f-col" style="left:937px;top:255px"><h3><i></i>Expo</h3><p>Lorem Ipsum is simply dummy text of the printing</p></div>
</footer>

<div class="bottom-bar">
  <p>© 2017 Carvelo Hub &nbsp;•&nbsp; Privacy Policy</p>
  <div class="social"><span></span><span></span><span></span><span></span><span></span><span></span></div>
</div>

</body>
</html>
```